Tarjetas de visita para empresa de aluminio

Empresa con mas de 40 años vendiendo perfiles de aluminio.
Somos fábrica y almacén, queremos renovar la tarjeta de presentación de nuestros comerciales dando una imgen innovadora y tecnógica mezclado con la calidez del respeto al medio ambiente.
Añado el logo de la empresa y actual cara trasera de la tarjeta de visita, el logo es el simbolo WM y la marca TRAVENIC EXTRUSION, la frase 2extrusion y lacado de aluminio" debe cambiarse por "Diseño, extrusión, lacado, anodizado y mecanizado de precisión de aluminio" o en su defecto incluir todos esos servicios que hacemos o una frase mas pegadiza.

We are an aluminium factory, we produce and stock profiles of aluminium.
we want to renew visit card of our sellers, we are looking for something that show innovation, tecnology and environment respect.
Upload our actual logo and back of visit card, logo WM and brand TRAVENIC EXTRUSION must be keept.
Text "Extrusion y lacado de aluminio" must be changed for "Diseño, extrusion, lacado, anodizado y mecanizado de precisión de aluminio" or something like that

```html
<!DOCTYPE html>
<html lang="es">
<head>
<meta charset="utf-8">
<title>Tarjetas de visita – Travenic Extrusion</title>
<link href="https://fonts.googleapis.com/css2?family=Oswald:wght@600&family=Roboto:wght@400;500&display=swap" rel="stylesheet">
<style>
  :root {
    --bg: #d9d9d9;
    --blue: #215480;
    --blue-dark: #1a4468;
    --white: #ffffff;
    --silver-light: #f2f2f2;
    --silver-mid: #a9adb0;
    --silver-dark: #5f6468;
    --ink-light: #ffffff;
  }
  * { margin: 0; padding: 0; box-sizing: border-box; }
  html, body { width: 1200px; height: 900px; overflow: hidden; }
  body {
    background: var(--bg);
    font-family: "Roboto", Arial, sans-serif;
    position: relative;
  }
  .card {
    position: absolute;
    left: 280px;
    width: 640px;
    height: 366px;
    overflow: hidden;
    box-shadow: 0 10px 24px rgba(0,0,0,0.18);
  }
  .card--back { top: 50px; background: var(--blue); }
  .card--front { top: 470px; background: var(--blue); }

  .pattern-field {
    position: absolute; inset: 0;
    background: linear-gradient(135deg, var(--blue) 0%, var(--blue-dark) 100%);
  }
  .brand-mark {
    position: absolute;
    display: flex; align-items: center; gap: 8px;
  }
  .brand-mark__circle {
    border: 2px solid var(--silver-light);
    border-radius: 50%;
  }
  .brand-mark__name {
    font-family: "Roboto", Arial, sans-serif;
    font-weight: 500;
    color: var(--silver-light);
    letter-spacing: 2px;
  }
  .card--back .brand-mark { right: 40px; bottom: 120px; }
  .card--back .brand-mark__circle { width: 26px; height: 26px; }
  .card--back .brand-mark__name { font-size: 26px; }

  .wave { position: absolute; inset: 0; }

  .identity { position: absolute; left: 40px; top: 48px; width: 320px; }
  .identity .brand-mark { position: static; margin-bottom: 10px; }
  .identity .brand-mark__circle { width: 22px; height: 22px; }
  .identity .brand-mark__name { font-size: 22px; letter-spacing: 3px; }
  .identity__tagline {
    color: var(--ink-light);
    font-size: 11px;
    line-height: 1.45;
    letter-spacing: 0.6px;
    text-transform: uppercase;
  }

  .address {
    position: absolute; left: 40px; bottom: 26px;
    color: var(--ink-light);
    font-size: 13px; line-height: 1.4;
    text-shadow: 0 1px 2px rgba(0,0,0,0.25);
  }

  .contact {
    position: absolute; right: 32px; top: 140px;
    text-align: right; color: var(--ink-light);
    text-shadow: 0 1px 2px rgba(0,0,0,0.3);
  }
  .contact__name {
    font-family: "Oswald", "Arial Narrow", sans-serif;
    font-weight: 600; font-size: 21px; letter-spacing: 0.5px;
  }
  .contact__role { font-size: 13px; margin-bottom: 10px; }
  .contact__list { list-style: none; font-size: 13px; line-height: 1.45; }
  .contact__list li { display: flex; justify-content: flex-end; align-items: center; gap: 8px; }
  .contact__icon { width: 11px; height: 11px; fill: var(--ink-light); }
</style>
</head>
<body>

<section class="card card--back" aria-label="Reverso de la tarjeta">
  <div class="pattern-field" role="img" aria-label="Fondo azul con patrón repetido del símbolo de la empresa"></div>
  <div class="brand-mark">
    <span class="brand-mark__circle"></span>
    <span class="brand-mark__name">WM</span>
  </div>
</section>

<section class="card card--front" aria-label="Anverso de la tarjeta">
  <svg class="wave" viewBox="0 0 640 366" preserveAspectRatio="none" aria-hidden="true">
    <defs>
      <linearGradient id="silver" x1="0" y1="1" x2="1" y2="0">
        <stop offset="0" stop-color="var(--silver-dark)"/>
        <stop offset="0.35" stop-color="var(--silver-mid)"/>
        <stop offset="0.55" stop-color="var(--silver-light)"/>
        <stop offset="0.8" stop-color="var(--silver-dark)"/>
        <stop offset="1" stop-color="var(--silver-light)"/>
      </linearGradient>
    </defs>
    <path d="M0,240 C180,225 300,215 370,140 C430,75 520,58 640,52 L640,366 L0,366 Z" fill="var(--white)"/>
    <path d="M0,258 C190,243 320,235 385,160 C445,92 530,78 640,72 L640,366 L0,366 Z" fill="url(#silver)"/>
  </svg>

  <div class="identity">
    <div class="brand-mark">
      <span class="brand-mark__circle"></span>
      <span class="brand-mark__name">TRAVENIC EXTRUSION</span>
    </div>
    <p class="identity__tagline">Diseño, extrusión, lacado, anodizado y<br>mecanizado de precisión de aluminio</p>
  </div>

  <address class="address" style="font-style:normal">
    Pol.Ind.Norte - C/4 Nº 12<br>
    28900 VILLANUEVA DEL RÍO (Madrid)<br>
    Apartado de Correos 245<br>
    www.travenic.com
  </address>

  <div class="contact">
    <div class="contact__name">MARCOS RUIZ DELGADO</div>
    <div class="contact__role">Comercial</div>
    <ul class="contact__list">
      <li>910 42 17 30
        <svg class="contact__icon" viewBox="0 0 12 12"><path d="M2.5 1l2 2-1 1.5c.8 1.6 1.9 2.7 3.5 3.5l1.5-1 2 2-1.5 2C5 10.5 1.5 7 1 2.5z"/></svg></li>
      <li>622 58 09 41
        <svg class="contact__icon" viewBox="0 0 12 12"><path d="M3 0h6v12H3zM4 1.5v8h4v-8z"/></svg></li>
      <li>910 42 17 39
        <svg class="contact__icon" viewBox="0 0 12 12"><path d="M3 0h6v3H3zM1 4h10v5H9v3H3V9H1zM4 8v3h4V8z"/></svg></li>
      <li>marcosruiz@travenic.com
        <svg class="contact__icon" viewBox="0 0 12 12"><path d="M0 2h12v8H0zM1 3v.5l5 3.2 5-3.2V3z"/></svg></li>
    </ul>
  </div>
</section>

</body>
</html>
```